Environmentally conscious Waste Management Company requires business card

We Require a Business card for our environmentally conscious waste management company . The business card should have a very clean design. be double sided and incorporate our logo..
The card will need o have 9 lines for the contact details - that are
Name
Title
Business
Address Line 1
Address Line 2
Address Line 3
Phone
Mobile
Email

Industry/Entity Type

Waste Management

Other font styles liked:
• Helvetica or similar

```html
<!DOCTYPE html>
<html lang="en">
<head>
<meta charset="utf-8">
<title>Tidyloop Business Card</title>
<link rel="stylesheet" href="https://fonts.googleapis.com/css2?family=Inter:wght@400;600&family=Michroma&display=swap">
<style>
  :root {
    --stage: #e4e4e2;
    --card-white: #f1f1f1;
    --brand-green: #18b932;
    --ink-dark: #2a2a2a;
    --ink-white: #ffffff;
  }
  * { box-sizing: border-box; margin: 0; padding: 0; }
  html, body { width: 1200px; height: 900px; overflow: hidden; }
  body {
    background: var(--stage);
    font-family: "Inter", Helvetica, Arial, sans-serif;
    display: flex;
    flex-direction: column;
    align-items: center;
    justify-content: center;
    gap: 52px;
  }
  .card {
    position: relative;
    width: 640px;
    height: 366px;
    background: var(--card-white);
    box-shadow: 0 6px 18px rgba(0,0,0,0.18);
    overflow: hidden;
  }
  .brand-name {
    color: var(--ink-dark);
    font-weight: 400;
    font-size: 34px;
    letter-spacing: 1px;
    line-height: 1;
    white-space: nowrap;
  }
  /* back side */
  .card-back .brand-name {
    position: absolute;
    left: 50%;
    top: 50%;
    transform: translate(-50%, -50%);
  }
  /* front side */
  .card-front .brand-name {
    position: absolute;
    left: 40px;
    top: 56px;
  }
  .green-band {
    position: absolute;
    left: 0;
    right: 0;
    top: 200px;
    bottom: 0;
    background: var(--brand-green);
  }
  .company-block {
    position: absolute;
    left: 40px;
    top: 214px;
    color: var(--ink-white);
    font-size: 10px;
    letter-spacing: 1.4px;
    line-height: 18px;
  }
  .company-name { font-weight: 600; }
  .person {
    position: absolute;
    right: 40px;
    top: 128px;
    text-align: right;
  }
  .person-name {
    font-family: "Michroma", "Inter", sans-serif;
    font-size: 19px;
    letter-spacing: 5px;
    color: var(--ink-dark);
  }
  .person-title {
    margin-top: 8px;
    font-size: 13px;
    letter-spacing: 4px;
    color: var(--brand-green);
  }
  .contact-list {
    position: absolute;
    right: 40px;
    bottom: 34px;
    list-style: none;
    color: var(--ink-white);
    font-size: 11px;
    letter-spacing: 2px;
  }
  .contact-list li {
    display: flex;
    justify-content: flex-end;
    align-items: center;
    gap: 14px;
    height: 24px;
  }
  .contact-icon {
    width: 14px;
    height: 14px;
    flex: none;
  }
</style>
</head>
<body>

  <section class="card card-back" aria-label="Business card back">
    <p class="brand-name">tidyloop</p>
  </section>

  <section class="card card-front" aria-label="Business card front">
    <div class="green-band"></div>

    <p class="brand-name">tidyloop</p>

    <div class="company-block">
      <p class="company-name">Tidyloop, Pty Ltd</p>
      <p>Address Line 1</p>
      <p>Address Line 2</p>
      <p>Address Line 3</p>
    </div>

    <div class="person">
      <p class="person-name">Mara Lind</p>
      <p class="person-title">Title</p>
    </div>

    <ul class="contact-list">
      <li>
        <span>555 010 2048</span>
        <svg class="contact-icon" viewBox="0 0 16 16" aria-label="Phone">
          <path d="M2 6c0-2 3-4 6-4s6 2 6 4v1h-3V5.5C10 5 9 4.8 8 4.8S6 5 5 5.5V7H2z" fill="var(--ink-dark)"/>
          <rect x="4" y="8" width="8" height="6" rx="1" fill="none" stroke="var(--ink-dark)" stroke-width="1.4"/>
        </svg>
      </li>
      <li>
        <span>555 010 2048</span>
        <svg class="contact-icon" viewBox="0 0 16 16" aria-label="Mobile">
          <rect x="4" y="1" width="8" height="14" rx="1.5" fill="none" stroke="var(--ink-dark)" stroke-width="1.4"/>
          <circle cx="8" cy="12.3" r="0.9" fill="var(--ink-dark)"/>
        </svg>
      </li>
      <li>
        <span>mara@tidyloop.com</span>
        <svg class="contact-icon" viewBox="0 0 16 16" aria-label="Email">
          <rect x="1.5" y="3.5" width="13" height="9" fill="none" stroke="var(--ink-dark)" stroke-width="1.4"/>
          <path d="M1.5 3.5 8 9l6.5-5.5" fill="none" stroke="var(--ink-dark)" stroke-width="1.4"/>
        </svg>
      </li>
    </ul>
  </section>

</body>
</html>
```